Zielgruppe
Wir sind ein junges Unternehmen im Bereich der Werbemittelbranche. Wir vertreiben u.a. Seccodosen im individuellen Design nach Kundenwunsch nur an B2B. Wir möchten eine Secco Dose entwickeln lassen, die
- als Eigenwerbung dienen soll (Abgabe an potentielle B2B Kunden ) und
- als Secco im Handel (Kioske, Touristshops B2C )
genutzt / verkauft werden kann.
Dies vor dem Hintergrund von möglichen sportlichen Großereignissen in Köln
(weitere Zielgruppenspezifische Ideen in Planung)
Aufgabenstellung
Entwicklung eines Dosenetiketts (PE-Kunststoffetikett) für eine 200 ML Secco Dose. Inhalt orginal italienischer IGT Secco Bianco.
Pflichttexte und Druckvorgaben/Stanze für Etikett wird geliefert.
Name: RheinPerlwein
Markantes plakatives Design.
Ggf. Nutzung der Kölner Signalfarben rot - schwarz- weiss
Hinweis zur Gestaltung - Optik.
Dosenmaterial Aluminium.
Es gibt 2 Optionen, die für die Gestaltung /Optik interessant sind:
1. Druck auf transparenter Folie. Optischer Eindruck wie ein Direktdruck auf Dose.
2. 1-4 C Druck auf weißer Folie

```html
<!DOCTYPE html>
<html lang="de">
<head>
<meta charset="utf-8">
<title>RheinPerlwein – Dosenetikett 200 ml</title>
<link href="https://fonts.googleapis.com/css2?family=Josefin+Sans:wght@400;700&family=Open+Sans:wght@400;700&display=swap" rel="stylesheet">
<style>
  :root {
    --page: #ffffff;
    --cologne-red: #df0000;
    --cologne-red-dark: #c20000;
    --label-black: #121212;
    --text-white: #ffffff;
    --legal-grey: #2a2a2a;
    --flag-green: #3cc04a;
    --flag-white: #f4f4f4;
    --flag-red: #e0262b;
  }
  * { margin: 0; padding: 0; box-sizing: border-box; }
  html, body {
    width: 1200px; height: 900px; overflow: hidden;
    background: var(--page);
  }
  .can-label {
    position: absolute;
    left: 200px; top: 166px;
    width: 800px; height: 466px;
    background: var(--label-black);
    box-shadow: 0 0 6px rgba(0,0,0,0.25);
    overflow: hidden;
  }
  .red-band {
    position: absolute; left: 0; top: 0;
    width: 100%; height: 175px;
    background: var(--cologne-red);
  }
  .seam-strip {
    position: absolute; right: 0; top: 0;
    width: 12px; height: 175px;
    background: var(--cologne-red-dark);
  }
  .brand-name {
    position: absolute;
    top: 104px;
    transform: translateX(-50%);
    font-family: "Josefin Sans", sans-serif;
    font-weight: 400;
    font-size: 36px;
    color: var(--text-white);
    white-space: nowrap;
  }
  .brand-name.front { left: 155px; }
  .brand-name.back { left: 500px; }
  .tricolore {
    position: absolute; left: 0; top: 254px;
    width: 710px; height: 8px;
    background: linear-gradient(to bottom,
      var(--flag-green) 0 3px,
      var(--flag-white) 3px 5px,
      var(--flag-red) 5px 8px);
    -webkit-mask-image: linear-gradient(to right, #000 85%, transparent);
            mask-image: linear-gradient(to right, #000 85%, transparent);
  }
  .product-line {
    position: absolute; top: 266px;
    transform: translateX(-50%);
    text-align: center;
    color: var(--text-white);
    white-space: nowrap;
  }
  .product-line.front { left: 158px; }
  .product-line.back { left: 504px; }
  .origin {
    font-family: "Open Sans", sans-serif;
    font-size: 13px;
    letter-spacing: 1.6px;
  }
  .variety {
    margin-top: 4px;
    font-family: "Josefin Sans", sans-serif;
    font-weight: 700;
    font-size: 15px;
    letter-spacing: 8.5px;
  }
  .legal-panel {
    position: absolute;
    left: 690px; top: 414px;
    width: 372px; height: 100px;
    transform-origin: top left;
    transform: rotate(-90deg);
    font-family: "Open Sans", sans-serif;
    color: var(--legal-grey);
  }
  .legal-copy {
    font-size: 8.4px;
    font-weight: 700;
    line-height: 13px;
    white-space: nowrap;
    overflow: hidden;
  }
  .legal-facts {
    display: flex;
    align-items: center;
    justify-content: space-between;
    margin-top: 3px;
    font-weight: 700;
    font-size: 15px;
  }
  .volume-group { display: flex; align-items: center; gap: 6px; }
  .estimated-sign { font-size: 19px; font-weight: 400; }
  .recycle-mark { width: 15px; height: 15px; margin-left: 6px; }
</style>
</head>
<body>
  <section class="can-label" aria-label="Dosenetikett RheinPerlwein Secco Bianco">
    <div class="red-band"></div>
    <div class="seam-strip"></div>

    <div class="brand-name front">RheinPerlwein</div>
    <div class="brand-name back">RheinPerlwein</div>

    <div class="tricolore"></div>

    <div class="product-line front">
      <p class="origin">Original italienischer</p>
      <p class="variety">SECCO BIANCO</p>
    </div>
    <div class="product-line back">
      <p class="origin">Original italienischer</p>
      <p class="variety">SECCO BIANCO</p>
    </div>

    <div class="legal-panel">
      <p class="legal-copy">RheinPerlwein – Vino Frizzante bianco IGT Veneto. Enthält Sulfite. Kühl lagern.</p>
      <p class="legal-copy">Aus italienischen Trauben. Gekühlt am besten genießen. Nach dem Öffnen leeren.</p>
      <p class="legal-copy">Abgefüllt für: Perlhaus Vertrieb GmbH · Domstraße 12 · 50667 Köln</p>
      <p class="legal-copy">www.rheinperlwein.de · Hergestellt in Italien · Pfandpflichtig</p>
      <div class="legal-facts">
        <span class="alcohol">10.5 % vol</span>
        <span class="volume-group">
          <span class="estimated-sign">℮</span>
          <span>200ml</span>
          <svg class="recycle-mark" viewBox="0 0 16 16" aria-hidden="true">
            <circle cx="8" cy="8" r="6.5" fill="none" stroke="currentColor" stroke-width="1.6"/>
            <path d="M5 9.5 L8 4.5 L11 9.5 Z" fill="none" stroke="currentColor" stroke-width="1.3"/>
          </svg>
        </span>
      </div>
    </div>
  </section>
</body>
</html>
```